Menu Re-Design for The Marbrook a british eatery in spanish holiday resort

Looking for a new design for our breakfast and lunch menu....

I have included some pictures of a few menus I like the feel of File No 1,2,3,4,5..... but am open to any ideas you may have....

The menu is to be double sided consisting of a front design with actual menu on reverse....

I have also included the relevant text files you will require...

We do not have a logo or set colour scheme to follow...

Target Market(s)

Predominantly British holidaymakers in popular Spanish resort....

Requirements
Must have
• Menu to be A3 and double sided, split between either a front page design and menu on reverse, or menu divided between both sides....
• Company Name:- The Marbrook
Nice to have
• Fun and Bold design whilst maintaining a feel of quality....
Should not have
• Please avoid the use of any food photography....

```html
<!DOCTYPE html>
<html lang="en">
<head>
<meta charset="utf-8">
<title>The Marbrook – Breakfasts and Lunch</title>
<link href="https://fonts.googleapis.com/css2?family=Lato:wght@300;400&family=Lobster&family=Open+Sans:ital,wght@0,400;1,400;1,600&family=Roboto:wght@500&display=swap" rel="stylesheet">
<style>
  :root {
    --orange: #e8562a;
    --red: #d7232f;
    --red-dark: #a8161f;
    --ink: #1c1c1c;
    --paper: #f1f1f1;
  }
  html, body { margin: 0; padding: 0; overflow: hidden; }
  body { width: 1200px; height: 848px; background: #fff; }
  .menu {
    position: relative; width: 1200px; height: 848px; overflow: hidden;
    background: var(--paper); color: var(--ink);
    font-family: "Roboto", Arial, sans-serif;
  }
  .pattern { position: absolute; inset: 0; background: radial-gradient(circle at 50% 50%, #f6f6f6, #ececec); }
  .brand {
    position: absolute; left: 20px; top: 14px; margin: 0;
    font-family: "Lato", sans-serif; font-weight: 400; font-size: 44px; color: #222;
  }
  .title {
    position: absolute; left: 0; right: 0; top: 62px; margin: 0; text-align: center;
    font-family: "Lobster", cursive; font-weight: 400; font-size: 62px; color: var(--orange);
  }
  .rule { position: absolute; height: 3px; border-top: 2px solid var(--orange); border-bottom: 2px solid var(--orange); }
  .daytime { position: absolute; left: 900px; top: 14px; width: 260px; height: 44px; }
  .daytime-label {
    position: absolute; left: 930px; top: 15px; width: 210px; text-align: center;
    font-family: "Open Sans", sans-serif; font-size: 22px; color: #fff;
  }
  .served {
    position: absolute; left: 930px; top: 54px; width: 210px; text-align: center;
    font-family: "Open Sans", sans-serif; font-size: 20px; color: #222;
  }
  .tag {
    position: absolute; background: var(--orange); color: #fff;
    font-family: "Lobster", cursive; font-size: 30px; text-align: center; line-height: 40px;
  }
  .col { position: absolute; }
  .row { display: flex; justify-content: space-between; font-size: 16.5px; font-weight: 500; }
  .desc { font-family: "Open Sans", sans-serif; font-style: italic; font-size: 13.5px; line-height: 19px; margin: 0; }
  .note { font-family: "Open Sans", sans-serif; font-size: 12.5px; margin: 1px 0 6px; }
  .strong-note { font-family: "Open Sans", sans-serif; font-style: italic; font-weight: 600; font-size: 13px; line-height: 19px; margin: 8px 0 0 14px; }
  .list .row { height: 23.6px; line-height: 23.6px; }
  .sub-head {
    position: absolute; left: 572px; top: 134px;
    font-family: "Lobster", cursive; font-size: 30px; color: var(--orange);
  }
  .min-order { position: absolute; left: 584px; top: 170px; font-family: "Open Sans", sans-serif; font-style: italic; font-size: 13px; }
  .dish { margin-bottom: 14px; }
  .burger-box {
    position: absolute; left: 817px; top: 456px; width: 348px; height: 344px;
    border: 2.5px solid var(--orange); box-sizing: border-box;
  }
  .extras .row { width: 222px; height: 23.8px; line-height: 23.8px; }
  .centre-note { font-family: "Open Sans", sans-serif; font-style: italic; font-weight: 600; font-size: 13px; text-align: center; }
</style>
</head>
<body>
<main class="menu">
  <div class="pattern" role="img" aria-label="Subtle pattern of concentric circles"></div>

  <h1 class="brand">The Marbrook</h1>
  <h2 class="title">Breakfasts and Lunch</h2>
  <div class="rule" style="left:30px; top:96px; width:272px;"></div>
  <div class="rule" style="left:890px; top:96px; width:282px;"></div>

  <svg class="daytime" viewBox="0 0 260 44" aria-hidden="true">
    <polygon points="0,10 32,10 32,40 0,40 10,25" fill="var(--red-dark)"/>
    <polygon points="260,10 228,10 228,40 260,40 250,25" fill="var(--red-dark)"/>
    <rect x="30" y="2" width="200" height="34" fill="var(--red)"/>
  </svg>
  <div class="daytime-label">Daytime menu</div>
  <div class="served">Served until 5pm</div>

  <!-- Left column -->
  <div class="tag" style="left:106px; top:148px; width:168px; transform:rotate(-3deg);">Breakfasts</div>
  <section class="col" style="left:15px; top:200px; width:371px;">
    <p class="desc">All our breakfast ingredients are of the highest quality available, sourced directly from the UK and freshly cooked to order</p>
    <div class="row" style="margin-top:6px;"><span>Marbrook</span><span>4.50</span></div>
    <p class="desc">Bacon, Fried Egg, Sausage, Beans or Grilled Tomato, Toast &amp; Butter</p>
    <p class="note">FREE Tea, Coffee or Orange Juice</p>
    <div class="row"><span>Jumbo</span><span>6.50</span></div>
    <p class="desc">2 Bacon, 2 Fried Eggs, 2 Sausage, Beans or Grilled Tomato, Toast &amp; Butter</p>
    <p class="note">FREE Tea, Coffee or Orange</p>
    <p class="strong-note">Any changes made to set breakfasts will be charged as build your own</p>
  </section>

  <div class="tag" style="left:80px; top:490px; width:250px; transform:rotate(3deg);">Breakfast Snacks</div>
  <section class="col list" style="left:15px; top:553px; width:369px;">
    <div class="row" style="height:24.6px;line-height:24.6px"><span>2 fried eggs on toast</span><span>3.50</span></div>
    <div class="row" style="height:24.6px;line-height:24.6px"><span>Scrambled eggs on toast</span><span>3.50</span></div>
    <div class="row" style="height:24.6px;line-height:24.6px"><span>Poached eggs on toast</span><span>4.00</span></div>
    <div class="row" style="height:24.6px;line-height:24.6px"><span>Beans on toast</span><span>3.50</span></div>
    <div class="row" style="height:24.6px;line-height:24.6px"><span>Toast and preserves</span><span>2.50</span></div>
    <div class="row" style="height:24.6px;line-height:24.6px"><span>Sausage sandwich</span><span>4.00</span></div>
    <div class="row" style="height:24.6px;line-height:24.6px"><span>Bacon sandwich</span><span>4.00</span></div>
    <div class="row" style="height:24.6px;line-height:24.6px"><span>Bacon &amp; Egg sandwich</span><span>4.50</span></div>
    <div class="row" style="height:24.6px;line-height:24.6px"><span>Sausage &amp; Egg sandwich</span><span>4.50</span></div>
    <div class="row" style="height:24.6px;line-height:24.6px"><span>Sausage &amp; Bacon sandwich</span><span>5.00</span></div>
  </section>

  <!-- Middle column -->
  <div class="rule" style="left:410px; top:152px; width:156px;"></div>
  <div class="sub-head">Build Your Own</div>
  <div class="min-order">Minimum order of 3.50 euros</div>
  <section class="col list" style="left:409px; top:191px; width:371px;">
    <div class="row"><span>Sausage</span><span>1.00</span></div>
    <div class="row"><span>Bacon</span><span>1.00</span></div>
    <div class="row"><span>Black Pudding</span><span>1.00</span></div>
    <div class="row"><span>Fried Bread</span><span>1.00</span></div>
    <div class="row"><span>Mushrooms</span><span>1.25</span></div>
    <div class="row"><span>Poached Egg</span><span>1.50</span></div>
    <div class="row"><span>Scrambled Eggs</span><span>2.00</span></div>
    <div class="row"><span>Fried Egg</span><span>75c</span></div>
    <div class="row"><span>Beans</span><span>50c</span></div>
    <div class="row"><span>Grilled Tomato</span><span>50c</span></div>
    <div class="row"><span>Hash Brown</span><span>75c</span></div>
    <div class="row"><span>2 Bread &amp; Butter</span><span>1.00</span></div>
    <div class="row"><span>2 Toast &amp; Butter</span><span>1.50</span></div>
  </section>

  <div class="tag" style="left:452px; top:512px; width:276px; transform:rotate(-4deg);">Something Different</div>
  <section class="col" style="left:409px; top:580px; width:371px;">
    <div class="dish">
      <div class="row"><span>Eggs Benedict</span><span>5.50</span></div>
      <p class="desc">traditional eggs benedict with home baked ham and soft poached eggs coated in a rich hollandaise sauce on a toasted english muffin</p>
    </div>
    <div class="dish">
      <div class="row"><span>Eggs Royale</span><span>6.00</span></div>
      <p class="desc" style="margin-top:6px">smoked salmon on a toasted english muffin softly poached eggs and a covering of hollandaise sauce</p>
    </div>
    <div class="dish">
      <div class="row"><span>Pancake Stack</span><span>6.50</span></div>
      <p class="desc">american style pancakes with crispy bacon and maple syrup</p>
    </div>
  </section>

  <!-- Right column -->
  <section class="col" style="left:806px; top:158px; width:370px;">
    <div class="dish" style="margin-bottom:18px">
      <div class="row"><span>Smoked and Scrambled</span><span>6.50</span></div>
      <p class="desc">smoked salmon with creamy scrambled eggs served with wholemeal toast</p>
    </div>
    <div class="dish" style="margin-bottom:28px">
      <div class="row"><span>Big Breakfast Wrap</span><span>5.50</span></div>
      <p class="desc">sausage bacon 2 egg omelette and hash brown served in a soft flour tortilla wrap</p>
    </div>
    <div class="dish">
      <div class="row"><span>Breakfast Muffin</span><span>5.00</span></div>
      <p class="desc">bacon or sausage on a toasted english muffin with mature cheddar cheese and a perfectly fried egg</p>
    </div>
  </section>

  <div class="burger-box"></div>
  <div class="tag" style="left:918px; top:440px; width:148px; transform:rotate(3deg);">Burgers</div>
  <section class="col" style="left:826px; top:486px; width:328px;">
    <div class="row" style="height:25px"><span>1/2 lb Homemade Aberdeen Angus</span><span>6.50</span></div>
    <div class="row" style="height:25px"><span>1/4 lb 100% Irish Beef</span><span>4.50</span></div>
    <div class="row" style="height:25px"><span>100% Chicken Breast (battered)</span><span>5.00</span></div>
    <p class="centre-note" style="margin:4px 0 18px">Add any extra of your choice</p>
    <div class="extras list" style="margin-left:44px">
      <div class="row"><span>Onion</span><span style="width:36px">50c</span></div>
      <div class="row"><span>Cheddar Cheese</span><span style="width:36px">1.00</span></div>
      <div class="row"><span>Onion Rings</span><span style="width:36px">1.00</span></div>
      <div class="row"><span>Bacon</span><span style="width:36px">1.00</span></div>
      <div class="row"><span>Chilli Con Carne</span><span style="width:36px">1.50</span></div>
      <div class="row"><span>Homemade Chips</span><span style="width:36px">2.00</span></div>
      <div class="row"><span>Spicy Potato Wedges</span><span style="width:36px">2.00</span></div>
    </div>
    <p class="centre-note" style="font-size:12px; margin-top:6px">All served with a salad garnish and homemade coleslaw</p>
  </section>
</main>
</body>
</html>
```